Natural Skincare Company Needs Label Design

We need a label design for the first product of a new company called 'Vela'. We make skincare products made from natural ingredients.
Our initial product is a rose hip oil, and we need a label for the small 30mL bottle that it comes in, as well as for the box that the bottle will be sold in. The label will be printed directly onto the bottle, like the example in the attached photo. For reference, we like the look and feel of the labels on the bottle and box in the attached photos. It should convey a sense of natural.
The bottle will be dark green glass. For the name 'Vela' we like something close to orange so that it stands out. The rest of the text on the front of the bottle and box should read 'natural skincare' 'pure & organic' 'Rose hip oil' 'huile de cynorrhodon' 'pure et biologique'. '30mL' '1fl.oz'
We also like the silhouette of the main ingredient like in the attached photo. So a silhouette of a rose hip on the front of the bottle and box would be preferred.
On the right side of the bottle and box:
'Rose hip oil'
'Ingredients: 100% natural, cold pressed, Rosa canina (rose hip) seed oil'
'Benefits: Hydrates and refreshes skin, leaving a more even skin tone and a healthy glow'
'Application: Massage 3-4 drops into clean, damp skin twice daily or as required'
'Suitable for all skin types'
'Store below 30C'
On the left side of the bottle and box:
'Huile de Cynorrhodon'
'Ingredients/Constituants: huile de Rosa canina (cynorrhodon) 100% naturel, presse a froid'
'Bienfaits: rafraichit la peau, teint eblouissant'
'Mode d'emploi: Massez 3 a 4 gouttes sur une peau propre et humide deluxe fois par jour'
'Convient a tous les types de peau'
'Conserver a moins de 30C'

```html
<!DOCTYPE html>
<html lang="en">
<head>
<meta charset="utf-8">
<title>Vela Rose Hip Oil – Bottle Label</title>
<link rel="stylesheet" href="https://fonts.googleapis.com/css2?family=Cinzel:wght@400&family=Crimson+Text:wght@400;600&display=swap">
<style>
  :root {
    --page: #ffffff;
    --panel-brown: #432407;
    --panel-orange: #e87e33;
    --cream: #f6ead9;
    --peach: #f3bd96;
    --mocha: #5b2f0d;
    --sprig-grey: #a08c7a;
    --white: #ffffff;
  }
  html, body {
    margin: 0;
    padding: 0;
    width: 1200px;
    height: 1000px;
    overflow: hidden;
    background: var(--page);
  }
  .canvas {
    position: relative;
    width: 1200px;
    height: 1000px;
  }
  .label {
    position: absolute;
    top: 128px;
    left: 40px;
    width: 1118px;
    height: 754px;
    display: flex;
  }
  .panel {
    position: relative;
    height: 100%;
  }
  .panel--side {
    width: 317px;
    background: var(--panel-brown);
  }
  .panel--right { width: 316px; }
  .panel--front {
    width: 485px;
    background: var(--panel-orange);
  }
  .sprig {
    position: absolute;
    display: block;
  }
  .panel--side .sprig {
    left: 122px;
    top: 124px;
    width: 96px;
    height: 78px;
  }
  .panel--front .sprig {
    left: 168px;
    top: 66px;
    width: 218px;
    height: 220px;
  }
  .wordmark {
    position: absolute;
    left: 0;
    right: 0;
    text-align: center;
    font-family: "Cinzel", serif;
    font-weight: 400;
    color: var(--white);
    margin: 0;
    line-height: 1;
  }
  .panel--side .wordmark {
    top: 214px;
    font-size: 42px;
    letter-spacing: 2px;
  }
  .panel--front .wordmark {
    top: 276px;
    font-size: 96px;
    letter-spacing: 4px;
  }
  .side-title {
    position: absolute;
    left: 0;
    right: 0;
    text-align: center;
    font-family: "Cinzel", serif;
    color: var(--cream);
    margin: 0;
    line-height: 1;
  }
  .side-title--fr {
    top: 269px;
    font-size: 14px;
    letter-spacing: 1.2px;
  }
  .side-title--en {
    top: 270px;
    font-size: 20px;
    letter-spacing: 0.5px;
  }
  .info {
    position: absolute;
    top: 324px;
    left: 53px;
    width: 218px;
    font-family: "Crimson Text", serif;
    font-size: 13.5px;
    line-height: 20px;
    color: var(--cream);
  }
  .panel--right .info { left: 59px; width: 210px; }
  .info p { margin: 0 0 20px; }
  .info b, .info .strong { font-weight: 600; }
  .front-text {
    position: absolute;
    left: 0;
    right: 0;
    text-align: center;
    font-family: "Cinzel", serif;
    margin: 0;
    line-height: 1;
  }
  .product-name {
    top: 396px;
    font-size: 40px;
    color: var(--mocha);
    letter-spacing: 1.5px;
  }
  .product-name-fr {
    top: 447px;
    font-size: 17px;
    color: var(--cream);
    letter-spacing: 2.5px;
  }
  .tagline {
    top: 547px;
    font-size: 12px;
    color: var(--mocha);
    letter-spacing: 3.5px;
  }
  .claim {
    font-size: 17px;
    color: var(--cream);
    letter-spacing: 2px;
  }
  .claim--en { top: 592px; }
  .claim--fr { top: 632px; }
  .claim-rule {
    position: absolute;
    top: 618px;
    left: 84px;
    width: 306px;
    height: 1.5px;
    background: var(--cream);
  }
  .volume {
    top: 680px;
    font-size: 13px;
    color: var(--mocha);
    letter-spacing: 2.5px;
  }
</style>
</head>
<body>
<div class="canvas">
  <div class="label">

    <section class="panel panel--side panel--left" lang="fr">
      <svg class="sprig" viewBox="0 0 96 78" role="img" aria-label="Rose hip sprig silhouette illustration">
        <rect width="96" height="78" rx="36" fill="var(--sprig-grey)" opacity="0.55"/>
      </svg>
      <h2 class="wordmark">Vela</h2>
      <p class="side-title side-title--fr">HUILE DE CYNORRHODON</p>
      <div class="info">
        <p><b>Ingredients/Constituants:</b> huile de Rosa canina (cynorrhodon) 100% naturel, presse a froid.</p>
        <p><b>Bienfaits:</b> rafraichit la peau, teint eblouissant</p>
        <p><b>Mode d'emploi:</b> Massez 3 a 4 gouttes sur une peau propre et humide deluxe fois par jour'</p>
        <p class="strong">Convient a tous les types de peau.</p>
        <p class="strong">Conserver a moins de 30C.</p>
      </div>
    </section>

    <section class="panel panel--front">
      <svg class="sprig" viewBox="0 0 218 220" role="img" aria-label="Rose hip branch silhouette with leaves and berries">
        <rect width="218" height="220" rx="100" fill="var(--peach)" opacity="0.6"/>
      </svg>
      <h1 class="wordmark">Vela</h1>
      <p class="front-text product-name">Rose hip oil</p>
      <p class="front-text product-name-fr" lang="fr">HUILE DE CYNORRHODON</p>
      <p class="front-text tagline">NATURAL SKINCARE</p>
      <p class="front-text claim claim--en">PURE &amp; ORGANIC</p>
      <div class="claim-rule"></div>
      <p class="front-text claim claim--fr" lang="fr">PURE ET BIOLOGIQUE</p>
      <p class="front-text volume">30ML 1FL.OZ</p>
    </section>

    <section class="panel panel--side panel--right">
      <svg class="sprig" viewBox="0 0 96 78" role="img" aria-label="Rose hip sprig silhouette illustration">
        <rect width="96" height="78" rx="36" fill="var(--sprig-grey)" opacity="0.55"/>
      </svg>
      <h2 class="wordmark">Vela</h2>
      <p class="side-title side-title--en">Rose hip oil</p>
      <div class="info">
        <p><b>Ingredients</b>: 100% natural, cold pressed, Rosa canina (rose hip) seed oil.</p>
        <p><b>Benefits:</b> Hydrates and refreshes skin, leaving a more even skin tone and a healthy glow.</p>
        <p><b>Application:</b> Massage 3-4 drops into clean, damp skin twice daily or as required.</p>
        <p class="strong">Suitable for all skin types.</p>
        <p class="strong">Store below 30C.</p>
      </div>
    </section>

  </div>
</div>
</body>
</html>
```